Business Package for Charitable Company
Lantern Drift
Business Package for Charitable Company - Fund Raising
Creative Brief
Professional
Peter Hollis
President
20400 SW Meadowlark Road Suite C Fernvale, OR 97000
555-xxx-xxxx
555-418-xxxx
Peter@lanterndrift.example
www.lanterndrift.example
Will need to get final project files in both AI and word Formatting should include sheet of cards(on 8x11) so can go to printer Letterhead email address needs to be info@lanterndrift.example. Front of Business Card needs to have main company logo. See attached. Also on Envelop no phone numbers or email Folder put place holder for a brief description of who we are on the back side of the folder. Inside location on right hand side provide area for card. Front cover include web address and email info@lanterndrift.example only no address phone number etc. Power Point Template that has title page, bullet page and conclusion page. To be clear we need the final deliverables: FRONT AND BACK BUSINESS CARD SIZE 10 ENVELOPE AND LETTER HEAD POWER POINT PRESENTATION TEMPLATE FOLDER DESIGN WITH FLAPS FOR HOLDING PROPOSAL PAPERWORK I have uploaded from a previous project the items that I need for this project to give you a idea of what I am looking for.
Please incorporate the full tagline information: Share Freely Lift Neighbors Build Futures Want options with all Black background and white and don't include logo image (ie circle) use the file I uploaded that shows lantern standing in as the first "I" in LANTERN in the back of the card until we can take a look at things.
markpdx markpdx
Designers, Please make sure that you use my upload for example only and provide your own creative layout and design I don't need it be the same. Thanks
FONTS AND COLORS FOR LOGO ARE: Font: PerpetuaTiltingMTBold GillSansMT Color: Brown: Pantone 4485 Orange: Pantone 180 Light Orange: Pantone 718 Yellow: Pantone 116

```html
<!DOCTYPE html>
<html lang="en">
<head>
<meta charset="utf-8">
<title>Lantern Drift – Business Cards</title>
<link rel="stylesheet" href="https://fonts.googleapis.com/css2?family=Cinzel:wght@700&family=Lato:wght@400;700&display=swap">
<style>
  :root {
    --bg: #8a8a8a;
    --card-white: #ffffff;
    --brown: #5a3d12;
    --black: #111111;
    --white: #ffffff;
    --orange: #e0701a;
    --orange-deep: #e06a10;
    --yellow: #f3c20c;
    --text-dark: #333333;
    --accent: #c9641a;
  }
  * { margin: 0; padding: 0; box-sizing: border-box; }
  html, body { width: 1200px; height: 751px; overflow: hidden; }
  body { background: var(--bg); position: relative; font-family: "Lato", sans-serif; }

  .card {
    position: absolute;
    width: 492px;
    height: 276px;
    border-radius: 12px;
    overflow: hidden;
  }
  .card--front { left: 72px; top: 67px; background: var(--card-white); }
  .card--brown { left: 631px; top: 67px; }
  .card--black { left: 72px; top: 403px; }
  .card--white { left: 631px; top: 403px; }
  .card--gradient { background: linear-gradient(90deg, var(--yellow) 0%, #f0a512 45%, var(--orange-deep) 100%); }

  /* Front card */
  .front__band {
    position: absolute; right: 0; top: 0; width: 130px; height: 100%;
    background: linear-gradient(90deg, rgba(243,194,12,0) 0%, var(--yellow) 30%, var(--orange-deep) 100%);
  }
  .front__figure {
    position: absolute; left: 362px; top: 0; width: 110px; height: 276px;
    background: linear-gradient(180deg, #9a7a1e 0%, #7a5f18 100%);
    border-radius: 40px 40px 0 0;
    opacity: 0.85;
  }
  .front__mark {
    position: absolute; left: 111px; top: 25px; width: 56px; height: 56px;
    border-radius: 50%; background: var(--orange);
  }
  .front__name {
    position: absolute; left: 34px; top: 92px;
    font-family: "Cinzel", serif; font-weight: 700; font-size: 27px;
    color: var(--brown); letter-spacing: 0.5px;
  }
  .front__motto {
    position: absolute; left: 36px; top: 128px;
    font-size: 9.5px; letter-spacing: 3px; color: var(--orange);
  }
  .front__person {
    position: absolute; left: 34px; top: 168px;
    font-family: "Cinzel", serif; font-weight: 700; font-size: 15px; color: var(--accent);
  }
  .front__person span { font-family: "Lato", sans-serif; font-weight: 400; font-size: 11px; color: var(--accent); }
  .front__contact {
    position: absolute; left: 34px; top: 196px; width: 320px;
    font-size: 10.5px; line-height: 19px; color: var(--text-dark);
  }
  .front__contact b { color: var(--accent); }

  /* Back cards */
  .logo {
    position: absolute; left: 0; right: 0; top: 106px; text-align: center;
  }
  .logo__name {
    font-family: "Cinzel", serif; font-weight: 700; font-size: 36px; letter-spacing: 0.5px; line-height: 1;
  }
  .logo__tagline {
    margin-top: 6px; font-weight: 700; font-size: 12.5px; letter-spacing: 0.3px;
  }
  .card--brown .logo__name, .card--brown .logo__tagline { color: var(--brown); }
  .card--black .logo__name, .card--black .logo__tagline { color: var(--black); }
  .card--white .logo__name, .card--white .logo__tagline { color: var(--white); }
</style>
</head>
<body>

  <section class="card card--front">
    <div class="front__band"></div>
    <div class="front__figure" role="img" aria-label="Silhouette of a hiker carrying a large backpack"></div>
    <div class="front__mark"></div>
    <div class="front__name">LANTERN DRIFT</div>
    <div class="front__motto">SHARE • LIFT • BUILD</div>
    <div class="front__person">Peter Hollis <span>- President</span></div>
    <div class="front__contact">
      <b>P:</b> 555-xxx-xxxx &nbsp;<b>F:</b> 555-418-xxxx<br>
      <b>E:</b> Peter@lanterndrift.example &nbsp;<b>W:</b> www.lanterndrift.example<br>
      20400 SW Meadowlark Road, Suite C, Fernvale, OR 97000
    </div>
  </section>

  <section class="card card--gradient card--brown">
    <div class="logo">
      <div class="logo__name">LANTERN DRIFT</div>
      <div class="logo__tagline">Share Freely - Lift Neighbors - Build Futures</div>
    </div>
  </section>

  <section class="card card--gradient card--black">
    <div class="logo">
      <div class="logo__name">LANTERN DRIFT</div>
      <div class="logo__tagline">Share Freely - Lift Neighbors - Build Futures</div>
    </div>
  </section>

  <section class="card card--gradient card--white">
    <div class="logo">
      <div class="logo__name">LANTERN DRIFT</div>
      <div class="logo__tagline">Share Freely - Lift Neighbors - Build Futures</div>
    </div>
  </section>

</body>
</html>
```